Games for Classrooms Website Redesign

The purpose of the website redesign is to freshen up the content and update it to give a more modern look and feel. It will show what we do concisely and satisfy all potential visitors. We work with primary schools and the brand is fun.About: Games for Classrooms is a scheme that brings top Zentara athletes into primary schools to inspire children to do more physical activity. We typically run a half day event at the school where the athlete does a fun fitness circuit with the children and then an inspirational assembly with a demonstration and Q&A. The children are asked to collect sponsorship money to take part in the event and a large proportion of the money raised goes back to the school in the form of a voucher for them to spend on new sports equipment. 1. To generate more leads from potential customers/schools2. To engage the children and parents more in the event and get them excited for their upcoming visit whilst setting up a fundraiser page.3. To simplify and modernise what is already there.

I have attached some ideas for each of the pages (uploaded in brief)

Here is a link to our current website: www.gamesforclassrooms.example

I have also attached a link to the sponsorship form which shows the kind of look and feel we're after.

Target Market(s)

Primary school teachers
Primary school parents

Number of Pages Required

5+ page

Requirements
Must have
• Fun, modern.
• Be built on plover scaffold

```html
<!DOCTYPE html>
<html lang="en">
<head>
<meta charset="utf-8">
<title>Activate – Games for Classrooms</title>
<link href="https://fonts.googleapis.com/css2?family=Figtree:wght@400;600;700;800&display=swap" rel="stylesheet">
<style>
:root{
  --red:#e30b2c;
  --pink:#f5a8b3;
  --pink-soft:rgba(245,168,179,.55);
  --orange:#ff6a17;
  --ink:#111111;
  --grey:#444444;
  --footer:#1e1e1e;
  --green:#3bb020;
  --white:#ffffff;
}
*{margin:0;padding:0;box-sizing:border-box}
html,body{width:725px;height:1200px;overflow:hidden}
body{position:relative;background:var(--white);font-family:"Figtree",Arial,sans-serif;color:var(--ink)}
.abs{position:absolute}
.site-header{position:absolute;left:0;top:0;width:725px;height:56px;border-bottom:1px solid #eee;background:var(--white);z-index:3}
.brand{position:absolute;left:40px;top:22px;display:flex;align-items:center;gap:6px;font-weight:800;font-size:8px;color:var(--ink);text-transform:uppercase}
.brand-dot{width:14px;height:14px;border-radius:50%;background:var(--red)}
.menu{position:absolute;right:50px;top:26px;display:flex;align-items:center;gap:8px;font-size:8px;font-weight:700;letter-spacing:.5px}
.menu svg{display:block}

.glow{position:absolute;border-radius:50%;background:radial-gradient(circle,var(--pink-soft) 0%,rgba(245,168,179,0) 70%);z-index:1}
.dot-grid{position:absolute;z-index:1}

.page-title{position:absolute;top:103px;width:725px;text-align:center;font-size:19px;font-weight:800;z-index:2}
.lead{position:absolute;top:190px;width:725px;text-align:center;font-size:11px;font-weight:700;line-height:13.5px;text-transform:uppercase;z-index:2}
.info-block{position:absolute;left:118px;width:240px;z-index:2}
.info-tag{display:inline-flex;align-items:center;height:17px}
.info-tag svg{margin-right:-2px}
.info-tag span{background:var(--red);color:var(--white);font-size:10px;font-weight:700;padding:0 10px 0 8px;height:17px;line-height:17px;border-radius:3px}
.info-text{margin:6px 0 0 15px;font-size:7px;line-height:8.7px;color:var(--grey);width:216px}
.video{position:absolute;left:413px;top:274px;width:224px;height:137px;border-radius:6px;background:linear-gradient(135deg,#8a5a3c,#c9a27a 45%,#6f8a5a);z-index:2}
.video-frame{position:absolute;left:408px;top:280px;width:220px;height:137px;border:1.5px solid var(--ink);border-radius:6px;z-index:1}
.play{position:absolute;left:98px;top:55px;width:26px;height:26px;border-radius:50%;background:rgba(255,255,255,.9)}
.play::after{content:"";position:absolute;left:10px;top:7px;border-left:9px solid var(--ink);border-top:6px solid transparent;border-bottom:6px solid transparent}
.lead-form{position:absolute;left:414px;top:430px;width:223px;height:220px;background:var(--red);border-radius:4px;z-index:2;padding:20px 26px 0 30px;color:var(--white)}
.form-frame{position:absolute;left:409px;top:437px;width:222px;height:218px;border:1.5px solid var(--ink);border-radius:4px;z-index:1}
.lead-form h2{font-size:14px;line-height:19px;font-weight:700;text-transform:uppercase}
.field{display:block;font-size:9px;border-bottom:1px solid rgba(255,255,255,.85);height:33.5px;padding-top:6px;width:166px}
.field:first-of-type{margin-top:2px}
.testimonials{position:absolute;left:0;top:752px;width:725px;height:226px;background:var(--orange);color:var(--white);z-index:2}
.testimonials h2{position:absolute;left:143px;top:25px;font-size:14px;line-height:17px;font-weight:700}
.quote-school{position:absolute;left:143px;top:92px;font-size:8.5px;font-weight:700}
.quote-body{position:absolute;left:143px;top:108px;width:430px;font-size:7px;line-height:9.5px}
.quote-name{position:absolute;left:143px;top:168px;font-size:7px;font-weight:700}
.dots{position:absolute;left:334px;top:197px;display:flex;gap:6px}
.dots i{display:block;width:10px;height:10px;border-radius:50%;background:rgba(255,255,255,.85)}
.dots i.on{background:var(--orange);border:2px solid #fff}
.site-footer{position:absolute;left:0;top:978px;width:725px;height:222px;background:var(--footer);color:var(--white);text-align:center;font-size:6px;letter-spacing:.3px;z-index:2}
.foot-links{position:absolute;top:22px;width:100%}
.foot-brand{position:absolute;top:57px;width:100%;display:flex;justify-content:center;align-items:center;gap:5px;font-weight:800;font-size:8px;text-transform:uppercase}
.foot-brand .brand-dot{width:12px;height:12px;background:var(--white)}
.foot-legal{position:absolute;top:86px;width:100%;line-height:8px}
.foot-contact{position:absolute;top:116px;width:100%;line-height:8.3px}
.foot-contact .lbl{color:var(--green)}
.social{position:absolute;top:166px;width:100%;display:flex;justify-content:center;gap:7px}
.social i{width:11px;height:11px;background:var(--green);border-radius:1px}
.copyright{position:absolute;top:197px;width:100%}
</style>
</head>
<body>

<header class="site-header">
  <div class="brand"><span class="brand-dot"></span>Games for Classrooms</div>
  <div class="menu">
    <svg width="22" height="10" viewBox="0 0 22 10" aria-hidden="true"><rect y="0" width="22" height="1.6" fill="#3bb020"/><rect y="4" width="22" height="1.6" fill="#2a8fe0"/><rect y="8" width="22" height="1.6" fill="#e30b2c"/></svg>
    MENU
  </div>
</header>

<div class="glow" style="left:600px;top:70px;width:160px;height:160px" aria-hidden="true"></div>
<div class="glow" style="left:-60px;top:180px;width:180px;height:140px" aria-hidden="true"></div>
<div class="glow" style="left:-50px;top:540px;width:190px;height:190px" aria-hidden="true"></div>
<div class="glow" style="left:560px;top:330px;width:150px;height:150px" aria-hidden="true"></div>
<div class="glow" style="left:570px;top:690px;width:110px;height:110px" aria-hidden="true"></div>

<svg class="dot-grid" style="left:300px;top:80px" width="125" height="60" viewBox="0 0 125 60" aria-hidden="true">
  <circle cx="4" cy="4" r="2.5" fill="#e30b2c"/>
  <circle cx="120" cy="8" r="2.5" fill="#e30b2c"/>
  <circle cx="10" cy="54" r="2" fill="#e30b2c"/>
  <circle cx="114" cy="50" r="2" fill="#e30b2c"/>
</svg>

<h1 class="page-title">ACTIVATE</h1>
<p class="lead">Athlete led whole school event that gets every<br>child inspired &amp; excited about beig active</p>

<section class="info-block" style="top:283px">
  <div class="info-tag"><svg width="11" height="13" viewBox="0 0 11 13" aria-hidden="true"><path d="M1 1 L10 6.5 L1 12 Z" fill="#fff" stroke="#111" stroke-width="1.5"/></svg><span>WHAT IS IT ?</span></div>
  <p class="info-text">Lorem ipsum dolor sit amet, consectetur adipiscing elit, sed do eiusmod tempor incididunt ut labore et dolore magna aliqua. Quis ipsum suspendisse ultrices gravida. Risus commodo viverra maecenas accumsan lacus vel facilisis. Lorem ipsum dolor sit amet, consectetur adipiscing elit, sed do eiusmod tempor incididunt ut labore et dolore magna aliqua. Quis ipsum</p>
</section>
<section class="info-block" style="top:380px">
  <div class="info-tag"><svg width="11" height="13" viewBox="0 0 11 13" aria-hidden="true"><path d="M1 1 L10 6.5 L1 12 Z" fill="#fff" stroke="#111" stroke-width="1.5"/></svg><span>WHY IS IT IMPORTANT ?</span></div>
  <p class="info-text">Lorem ipsum dolor sit amet, consectetur adipiscing elit, sed do eiusmod tempor incididunt ut labore et dolore magna aliqua. Quis ipsum suspendisse ultrices gravida. Risus commodo viverra maecenas accumsan lacus vel facilisis. Lorem ipsum dolor sit amet, consectetur adipiscing elit, sed do eiusmod tempor incididunt ut labore et dolore magna aliqua. Quis ipsum</p>
</section>
<section class="info-block" style="top:476px">
  <div class="info-tag"><svg width="11" height="13" viewBox="0 0 11 13" aria-hidden="true"><path d="M1 1 L10 6.5 L1 12 Z" fill="#fff" stroke="#111" stroke-width="1.5"/></svg><span>HOW MUCH DOES IT COST ?</span></div>
  <p class="info-text">Lorem ipsum dolor sit amet, consectetur adipiscing elit, sed do eiusmod tempor incididunt ut labore et dolore magna aliqua. Quis ipsum suspendisse ultrices gravida. Risus commodo viverra maecenas accumsan lacus vel facilisis. Lorem ipsum dolor sit amet, consectetur adipiscing elit, sed do eiusmod tempor incididunt ut labore et dolore magna aliqua. Quis ipsum</p>
</section>
<section class="info-block" style="top:571px">
  <div class="info-tag"><svg width="11" height="13" viewBox="0 0 11 13" aria-hidden="true"><path d="M1 1 L10 6.5 L1 12 Z" fill="#fff" stroke="#111" stroke-width="1.5"/></svg><span>WHO IS WILLING TO BE ?</span></div>
  <p class="info-text">Lorem ipsum dolor sit amet, consectetur adipiscing elit, sed do eiusmod tempor incididunt ut labore et dolore magna aliqua. Quis ipsum suspendisse ultrices gravida. Risus commodo viverra maecenas accumsan lacus vel facilisis. Lorem ipsum dolor sit amet, consectetur adipiscing elit, sed do eiusmod tempor incididunt ut labore et dolore magna aliqua. Quis ipsum</p>
</section>

<div class="video-frame"></div>
<div class="video" role="img" aria-label="Video still of children doing a fitness circuit in a school hall"><span class="play"></span></div>

<div class="form-frame"></div>
<form class="lead-form">
  <h2>Find out when we’re<br>next to your area...</h2>
  <label class="field">Name</label>
  <label class="field">School</label>
  <label class="field">Postcode</label>
  <label class="field">Best Time to Call</label>
</form>

<section class="testimonials">
  <svg class="abs" style="left:85px;top:13px" width="60" height="70" viewBox="0 0 60 70" aria-hidden="true"><path d="M4 4h24v28h-12c0 14 4 22 12 24v10c-18-2-24-16-24-34Z M32 4h24v28h-12c0 14 4 22 12 24v10c-18-2-24-16-24-34Z" fill="rgba(255,255,255,.18)"/></svg>
  <svg class="abs" style="left:558px;top:106px" width="80" height="84" viewBox="0 0 80 84" aria-hidden="true"><path d="M76 80H48V46h14c0-16-4-26-14-28V6c22 2 28 20 28 40Z M38 80H10V46h14c0-16-4-26-14-28V6c22 2 28 20 28 40Z" fill="rgba(255,255,255,.18)"/></svg>
  <h2>We’re really proud of our unprompted and unedited feedback.<br>Here’s what are schools have said about us...</h2>
  <p class="quote-school">Elmfield Infants’ School (23rd June 2018)</p>
  <p class="quote-body">I just wanted to say thank you for such a fabulous day on Friday. It was absolutely brilliant from start to finish and it ran so smoothly. Everyone commented on how professional and inspirational the whole day was. Marcus’s assembly was just perfect, we really couldn’t have asked for a better day. When I went out to the playground at lunch time, I saw so many children practising their triple jump and encouraging others to join in – what more could we ask for? I am hoping that we will be able to have you in again at some point next year as the day was such a success. Thank you once again.</p>
  <p class="quote-name">Jo (PE Coordinator)</p>
  <div class="dots"><i></i><i></i><i></i><i class="on"></i></div>
</section>

<footer class="site-footer">
  <p class="foot-links">SITEMAP I COOKIES I PRIVACY POLICY I ONLINE FUNDRAISING</p>
  <div class="foot-brand"><span class="brand-dot"></span>Games for Classrooms</div>
  <p class="foot-legal">Games for Classrooms and GFC Coaching are trading names of the Social Enterprise<br>called Playmotive Limited, a company registered in England no. 01234567.</p>
  <p class="foot-contact"><span class="lbl">Telephone:</span> 01632 960400 (GB) or 01 555 0182 (Ireland)<br><span class="lbl">Email:</span> hello@gamesforclassrooms.example<br><span class="lbl">Snailmail (we love a letter!):</span><br>GAMES for CLASSROOMS 7 Brook Yard, Fenway Park Estate, Northby NB1 2AA<br>GAMES for CLASSROOMS Harbour House, Quay Lane, Westport 4 Ireland</p>
  <div class="social"><i></i><i></i><i></i></div>
  <p class="copyright">© 2019 GAMES FOR CLASSROOMS</p>
</footer>

</body>
</html>
```